High-Class Professional Letterhead for a solo doctor's practice.

Please create a letterhead design that includes my logo, and options of my light blue/black color scheme and black and gold so I can choose between the two. I would like my Contact information on the top or bottom of the letterhead somewhere:
Delia Forsk, M.D.
Hand and Upper Extremity Surgeon
4382 NW 58th Lane, Suite 307
Tamarac, FL 33498
Phone: (954) 316-8842
Fax: (800) 629-4087
www.dforskgrip.example

Also on the bottom of the letterhead, there should be 2 different versions:
one that is blank, and one that has a signature spot on the bottom so I can sign:
Delia Forsk, M.D.
Board Certified Orthopaedic Hand Surgeon

I am going for classy/professional. I want other doctors and or lawyers to look at my letterhead and want to work with me. Again, professional, classy, clean. I do like black and gold but I could see what the blue like my other business card looks like too. Please do what most people do for letterheads--I'm not sure if the signature line should be on there? Or should be blank? I have no clue

Target Market(s)

Doctors and Lawyers

Industry/Entity Type

Medicine

Colors
0054AA
0677BA
7BADD7
CADEEF
E8F1F8

Requirements
Must have
• High class, professional, appealing

```html
<!DOCTYPE html>
<html lang="en">
<head>
<meta charset="utf-8">
<title>Delia Forsk, M.D. — Letterhead</title>
<link rel="stylesheet" href="https://fonts.googleapis.com/css2?family=Montserrat:wght@400;500;700&display=swap">
<style>
  :root {
    --backdrop: #e9e9ea;
    --paper: #ffffff;
    --ink: #1f1f1f;
    --ink-soft: #3a3a3a;
    --gold: #d4b983;
    --watermark: #f1f1f1;
  }
  * { box-sizing: border-box; margin: 0; padding: 0; }
  html, body { width: 1200px; height: 874px; overflow: hidden; }
  body {
    background: var(--backdrop);
    font-family: "Montserrat", sans-serif;
    color: var(--ink);
    display: flex;
    align-items: center;
    justify-content: center;
  }
  .letterhead {
    position: relative;
    width: 594px;
    height: 840px;
    background: var(--paper);
    box-shadow: 0 2px 10px rgba(0,0,0,0.08);
    overflow: hidden;
  }
  .watermark {
    position: absolute;
    left: 250px;
    top: 330px;
    width: 300px;
    height: 300px;
    border-radius: 50%;
    border: 14px solid var(--watermark);
    display: flex;
    align-items: center;
    justify-content: center;
    font-size: 34px;
    font-weight: 500;
    color: var(--watermark);
    letter-spacing: 2px;
  }
  .brand {
    position: absolute;
    left: 40px;
    top: 48px;
    display: flex;
    align-items: center;
    gap: 10px;
  }
  .brand-circle {
    width: 62px;
    height: 62px;
    border-radius: 50%;
    border: 4px solid var(--ink);
  }
  .brand-name {
    font-size: 15px;
    font-weight: 700;
    letter-spacing: 2px;
    text-transform: uppercase;
  }
  .contact {
    position: absolute;
    left: 350px;
    top: 40px;
    padding-left: 16px;
    border-left: 1px solid var(--ink);
    font-size: 9px;
    line-height: 1.45;
    color: var(--ink-soft);
  }
  .contact-name { font-weight: 700; font-size: 10.5px; color: var(--ink); }
  .contact-line { display: flex; align-items: center; gap: 5px; }
  .contact-line svg { width: 8px; height: 8px; fill: var(--ink); }
  .recipient {
    position: absolute;
    left: 60px;
    top: 240px;
    font-size: 10.5px;
    line-height: 1.5;
  }
  .body-copy {
    position: absolute;
    left: 60px;
    top: 330px;
    width: 480px;
    font-size: 10px;
    line-height: 1.6;
    color: var(--ink);
  }
  .body-copy p { margin-bottom: 22px; }
  .signoff { font-size: 10.5px; }
  .signature {
    margin-top: 10px;
    width: 130px;
    height: 18px;
    background: #f0f0f0;
  }
  .signature-title { font-size: 6.5px; color: var(--ink-soft); margin-top: 2px; }
  .footer-rule {
    position: absolute;
    left: 220px;
    right: 40px;
    bottom: 52px;
    height: 1px;
    background: var(--gold);
  }
</style>
</head>
<body>
  <main class="letterhead">
    <div class="watermark" aria-hidden="true">Forsk Hand</div>

    <header>
      <div class="brand">
        <div class="brand-circle"></div>
        <div class="brand-name">Forsk Hand</div>
      </div>

      <address class="contact">
        <div class="contact-name">Delia Forsk, M.D.</div>
        <div>Hand and Upper Extremity Surgeon</div>
        <div>4382 NW 58th Lane, Suite 307</div>
        <div>Tamarac, FL 33498</div>
        <div class="contact-line">
          <svg viewBox="0 0 24 24"><path d="M6.6 10.8a15 15 0 0 0 6.6 6.6l2.2-2.2a1 1 0 0 1 1-.25 11.4 11.4 0 0 0 3.6.6 1 1 0 0 1 1 1V20a1 1 0 0 1-1 1A17 17 0 0 1 3 4a1 1 0 0 1 1-1h3.5a1 1 0 0 1 1 1 11.4 11.4 0 0 0 .6 3.6 1 1 0 0 1-.25 1z"/></svg>
          (954) 316-8842
        </div>
        <div class="contact-line">
          <svg viewBox="0 0 24 24"><path d="M6 2h10v6H6zM4 9h16a2 2 0 0 1 2 2v7h-4v4H6v-4H2v-7a2 2 0 0 1 2-2zm4 8v3h8v-3z"/></svg>
          (800) 629-4087
        </div>
        <div class="contact-line">
          <svg viewBox="0 0 24 24"><circle cx="12" cy="12" r="10"/></svg>
          www.dforskgrip.example
        </div>
      </address>
    </header>

    <section class="recipient">
      <div>Mr/s</div>
      <div>First Name and Last Name</div>
      <div>Company Name</div>
      <div>Address</div>
    </section>

    <section class="body-copy">
      <p>Lorem Ipsum is simply dummy text of the printing and typesetting industry. Lorem Ipsum has been the industry's standard dummy text ever since the 1500s, when an unknown printer took a galley of type and scrambled it to make a type specimen book. It has survived not only five centuries, but also the leap into electronic typesetting, remaining essentially unchanged. It was popularised in the 1960s with the release of Letraset sheets containing Lorem Ipsum passages.</p>
      <p>The standard chunk of Lorem Ipsum used since the 1500s is reproduced below for those interested. Sections 1.10.32 and 1.10.33 from "de Finibus Bonorum et Malorum" by Cicero are also reproduced in their exact original form, accompanied by English versions from the 1914 translation by H. Rackham. Lorem ipsum dolor sit amet, consectetur adipiscing elit, sed do eiusmod tempor incididunt ut labore et dolore magna aliqua.</p>
      <p>It is a long established fact that a reader will be distracted by the readable content of a page when looking at its layout. The point of using Lorem Ipsum is that it has a more-or-less normal distribution of letters, as opposed to using 'Content here, content here', making it look like readable English. Many desktop publishing packages and web page editors now .</p>
      <div class="signoff">Your Sincerely,</div>
      <div class="signature" role="img" aria-label="Handwritten signature of Delia Forsk, M.D."></div>
      <div class="signature-title">Board Certified Orthopaedic Hand Surgeon</div>
    </section>

    <div class="footer-rule"></div>
  </main>
</body>
</html>
```